Graphic or Colorful Core Values Wall

I need artwork for an executive conference room wall. It is the blank space between the window and bookshelf (some photos have a blue 24x48 paper taped to the wall). I'm open to material options. The room has metal, wood, acrylic, black, silver, navy blue, saddle leather chairs, and a white conference table. There will be a sideboard/table below the artwork for balance. Not sure what that'll look like yet. You can see the mockups in the pdfs. You can read more about our heritage at dervy.com. <-- Feel free to use imagery from here if need be.

We have been around since 1929 so anything historical is fair game. We built the shell-shaped marlin station in Winston-Salem, NC (only 1 remains today) However we have diversified greatly since then.

Target Market(s)

Executives

Font styles to use
Sans Serif
Other font styles liked:
• Century Gothic for the main font, "Since 1929" is in Jelytta

Requirements
Must have
• The artwork or graphic must include the following Core Values: do it because it is right treat customers, vendors, and fellow employees as we would like to be treated be financially responsible be better today than yesterday Vision: To be the best at what we choose to do as recognized by our co-workers, customers, and competitors. Mission: To expand and develop our company through strict adherence to our "Core Ideology." We will empower, train, and motivate "Quality People" to strive for operational excellence.
Nice to have
• Owner likes color but the room doesn't have much color. Our logo has Red: #E10920 and Yellow: #FCBF15 in it
Should not have
• Look through our website and see how we use primary colors. We need to stay on brand as well as fit the room.

```html
<!DOCTYPE html>
<html lang="en">
<head>
<meta charset="utf-8">
<title>Core Values, Vision and Mission Posters</title>
<link href="https://fonts.googleapis.com/css2?family=Jost:wght@400;500;600;700&family=Courier+Prime:wght@400;700&display=swap" rel="stylesheet">
<style>
  :root {
    --navy: #262b6e;
    --yellow: #fcbf15;
    --red: #e10920;
    --white: #ffffff;
    --outline: #5560a8;
    --ring: #7e8ad8;
    --backdrop: #e8e5e0;
    --sans: "Jost", "Century Gothic", sans-serif;
    --mono: "Courier Prime", "Courier New", monospace;
  }
  * { box-sizing: border-box; margin: 0; padding: 0; }
  html, body { width: 1200px; height: 900px; overflow: hidden; }
  body { background: var(--backdrop); position: relative; font-family: var(--sans); }

  .poster {
    position: absolute;
    top: 215px;
    width: 330px;
    height: 470px;
    background: var(--navy);
    overflow: hidden;
  }
  .poster--values { left: 45px; }
  .poster--vision { left: 435px; }
  .poster--mission { left: 825px; }

  .abs { position: absolute; line-height: 1; white-space: nowrap; }
  .mono { font-family: var(--mono); font-size: 11px; line-height: 14px; }

  /* Core values poster */
  .values-band {
    position: absolute; left: 22px; top: 0; width: 20px; height: 157px;
    background: var(--yellow);
    display: flex; align-items: center; justify-content: center;
  }
  .values-band__label {
    writing-mode: vertical-rl; transform: rotate(180deg);
    color: var(--navy); font-weight: 500; font-size: 14px; letter-spacing: .3px;
  }
  .value-heading { color: var(--yellow); font-weight: 600; font-size: 36px; }
  .value-heading--do { left: 0; width: 100%; text-align: center; top: 44px; }
  .value-heading--treat { left: 0; width: 100%; text-align: center; top: 347px; }
  .value-sub { color: var(--white); text-align: center; left: 0; width: 100%; }
  .value-sub--do { top: 88px; }
  .value-sub--treat { top: 392px; white-space: normal; padding: 0 70px; }

  .numeral { font-weight: 600; font-size: 112px; }
  .numeral--one { left: 138px; top: 108px; color: var(--white); }
  .numeral--two { left: 152px; top: 146px; color: var(--yellow); }
  .numeral--three { left: 114px; top: 186px; color: var(--red); }
  .numeral--four { left: 148px; top: 232px; color: var(--white); }
  .value-be { font-weight: 600; font-size: 34px; }
  .value-be--financial { left: 212px; top: 163px; color: var(--red); }
  .value-be--better { left: 70px; top: 236px; color: var(--white); }
  .value-note--financial { left: 212px; top: 194px; color: var(--white); }
  .value-note--better { right: 211px; top: 268px; color: var(--yellow); text-align: right; }

  /* Vision poster */
  .vision-word { left: 0; width: 100%; text-align: center; font-weight: 700; letter-spacing: -2px; }
  .vision-word--solid { color: var(--white); font-size: 112px; }
  .vision-word--outline { color: transparent; -webkit-text-stroke: 1.2px var(--outline); font-weight: 500; font-size: 80px; letter-spacing: -1px; }
  .vision-word--top { top: -22px; }
  .vision-word--top-echo { top: 82px; }
  .vision-word--bottom-echo { top: 290px; transform: rotate(180deg); }
  .vision-word--bottom { top: 372px; transform: rotate(180deg); }
  .vision-o { position: relative; }
  .vision-word--solid .vision-o::after {
    content: ""; position: absolute; left: 50%; top: 57%;
    width: 22px; height: 22px; border-radius: 50%;
    background: var(--yellow); transform: translate(-50%, -50%);
  }
  .vision-statement {
    left: 0; width: 100%; top: 216px; text-align: center;
    color: var(--yellow); white-space: normal; padding: 0 44px;
  }

  /* Mission poster */
  .mission-title {
    position: absolute; left: 22px; top: 22px; height: 420px; z-index: 0;
    writing-mode: vertical-rl; transform: rotate(180deg);
    color: var(--white); font-weight: 700; font-size: 96px; line-height: 1;
    letter-spacing: -1px; text-align: left;
  }
  .mission-o { position: relative; }
  .mission-o::before {
    content: ""; position: absolute; left: 50%; top: 50%;
    width: 92px; height: 92px; border-radius: 50%;
    background: var(--ring); transform: translate(-50%, -50%); z-index: -1;
  }
  .mission-quote { left: 142px; top: 118px; color: var(--yellow); font-weight: 700; font-size: 110px; }
  .mission-text { left: 145px; color: var(--white); white-space: normal; width: 160px; }
  .mission-text--first { top: 216px; }
  .mission-text--second { top: 290px; }
</style>
</head>
<body>

<section class="poster poster--values">
  <div class="values-band"><span class="values-band__label">Core Values</span></div>

  <h2 class="abs value-heading value-heading--do">Do It</h2>
  <p class="abs mono value-sub value-sub--do">Because It Is Right</p>

  <span class="abs numeral numeral--one">1</span>
  <span class="abs numeral numeral--two">2</span>
  <span class="abs numeral numeral--three">3</span>
  <span class="abs numeral numeral--four">4</span>

  <span class="abs value-be value-be--financial">be</span>
  <p class="abs mono value-note--financial">Financially<br>Responsible</p>

  <span class="abs value-be value-be--better">Be</span>
  <p class="abs mono value-note--better">Better<br>Today Than<br>Yesterday</p>

  <h2 class="abs value-heading value-heading--treat">Treat</h2>
  <p class="abs mono value-sub value-sub--treat">Customers, Vendors, And Fellow Employees As We Would Like To Be Treated</p>
</section>

<section class="poster poster--vision">
  <h2 class="abs vision-word vision-word--solid vision-word--top">Visi<span class="vision-o">o</span>n</h2>
  <span class="abs vision-word vision-word--outline vision-word--top-echo" aria-hidden="true">Vision</span>
  <p class="abs mono vision-statement">To be the best at what we choose to do as recognized by our co-workers, customers, and competitors</p>
  <span class="abs vision-word vision-word--outline vision-word--bottom-echo" aria-hidden="true">Vision</span>
  <span class="abs vision-word vision-word--solid vision-word--bottom" aria-hidden="true">Visi<span class="vision-o">o</span>n</span>
</section>

<section class="poster poster--mission">
  <h2 class="mission-title">Missi<span class="mission-o">o</span>n</h2>
  <span class="abs mission-quote" aria-hidden="true">&ldquo;</span>
  <p class="abs mono mission-text mission-text--first">To expand and develop our company through strict adherence to our "Core Ideolgy."</p>
  <p class="abs mono mission-text mission-text--second">We will empower, train, and motivate "Quality People" to strive for operational excellence</p>
</section>

</body>
</html>
```